Business Image

I have recently had a new company logo made up and require some new business cards to go with it.

Target Market(s)

Developers & high worth clients.

Industry/Entity Type

Business

Contact Information for Business Card

The business is in the construction/management industry. It needs to be classy but have a industrial feel. I would like the business card to be a elegant presentation in itself.

Requirements
Must have
• Current logo & company name. Colouring needs to be the same as the current design also.
Nice to have
• A few different designs & presentations of single and double sided business cards.

```html
<!DOCTYPE html>
<html lang="en">
<head>
<meta charset="utf-8">
<title>Keystone Build Partners – Business Card</title>
<link href="https://fonts.googleapis.com/css2?family=Open+Sans:wght@400;600;700&display=swap" rel="stylesheet">
<style>
  :root {
    --backdrop: #e4e2dd;
    --paper: #f2f1ed;
    --edge: #1b7fa3;
    --brand-navy: #1d4f7c;
    --ink: #2b2b2b;
    --rule: #8a8a88;
  }
  * { box-sizing: border-box; margin: 0; padding: 0; }
  html, body {
    width: 1200px; height: 919px; overflow: hidden;
    background: var(--backdrop);
    font-family: "Open Sans", Arial, sans-serif;
    color: var(--ink);
  }
  .canvas {
    position: relative; width: 1200px; height: 919px;
    display: flex; flex-direction: column; align-items: center; justify-content: center; gap: 64px;
  }
  .card {
    position: relative; width: 560px; height: 320px;
    background: var(--paper);
    border-bottom: 6px solid var(--edge);
    box-shadow: 0 10px 24px rgba(0,0,0,0.12);
  }
  .brand {
    display: flex; flex-direction: column; align-items: center;
  }
  .brand-square {
    width: 40px; height: 40px; background: var(--brand-navy); margin-bottom: 14px;
  }
  .brand-name {
    font-weight: 600; color: var(--brand-navy);
    letter-spacing: 2px; text-transform: uppercase; text-align: center;
  }
  .card-front { display: flex; align-items: center; justify-content: center; }
  .card-front .brand-name { font-size: 30px; }

  .card-back .brand { position: absolute; top: 34px; left: 0; right: 0; }
  .card-back .brand-square { width: 30px; height: 30px; margin-bottom: 10px; }
  .card-back .brand-name { font-size: 21px; }
  .rule {
    position: absolute; left: 0; right: 0; height: 0;
    border-top: 1px solid var(--rule);
    box-shadow: 0 3px 0 -2px var(--rule);
  }
  .rule-top { top: 86px; }
  .rule-bottom { top: 268px; }
  .contact {
    position: absolute; top: 150px; left: 0; right: 0; text-align: center;
    font-size: 14px; line-height: 1.55;
  }
  .person { font-size: 16px; margin-bottom: 10px; }
  .person-name { font-weight: 700; color: var(--brand-navy); }
  .label { font-weight: 700; color: var(--brand-navy); }
</style>
</head>
<body>
<main class="canvas">
  <section class="card card-front" aria-label="Card front">
    <div class="brand">
      <div class="brand-square"></div>
      <div class="brand-name">Keystone Build Partners</div>
    </div>
  </section>

  <section class="card card-back" aria-label="Card back">
    <div class="brand">
      <div class="brand-square"></div>
      <div class="brand-name">Keystone Build Partners</div>
    </div>
    <div class="rule rule-top" style="top:138px"></div>
    <div class="contact" style="top:150px">
      <p class="person"><span class="person-name">DANIEL HARROW</span> - CEO/FOUNDER</p>
      <p>4120 Birchwood Court, Juneau, Alaska 99801</p>
      <p><span class="label">P:</span> 907 512 4476 <span class="label">M:</span> 907 338 2105 <span class="label">F:</span> 907 264 7819</p>
      <p><span class="label">E:</span> daniel@keystonebuild.com <span class="label">W:</span> www.keystonebuild.com</p>
    </div>
    <div class="rule rule-bottom" style="top:284px"></div>
  </section>
</main>
</body>
</html>
```